Say goodbye to Paper Cuts - Modern B2B Paper Ad

We need a design for a full page magazine ad

Company Overview:
Quillbright is an administration support company for Harbourline Lending Agents. We are running a full page ad in Harbourline Lending Agents magazine

Ad Copy
"Say Goodbye to Paper Cuts"
"On-Demand Admin Support for Mortgage Professionals"
[website url at the bottom]

Ad Dimensions:
Trim: (w) 8.25” x (h) 10.875”
Bleed: (w) 8.75” x (h) 11.375”
Type: (w) 7.5” x (h) 10.125”

Ad Requirements (provided by the magazine)
Please supply all artwork in PC format only, either in EPS, Tiff or PDF format with the following requirements:

- All files must be 300 dpi high resolution with CMYK process colour.
- Any Pantone colours that are found will automatically be converted to CMYK. Please double check that all colours are in CMYK.
- EPS files must be in outline path for all fonts and embedded images.
- Tiff files must be in PC format, flatten with no layer.
- PDF files must be press optimized and embedded with images and fonts.
- All Double page ads and Full page ads must be in press-optimized PDF files.
- 0.125" bleed with crop marks are required for Double page ads, Full page ads and Panel ads to be supplied on artwork where specified.
- Ad files in Microsoft Word, Excel, PowerPoint or other software are NOT acceptable.
- Materials received should be in a printable file with no conversion required.

Industry/Entity Type

It Company

Font styles to use
Sans Serif

Requirements
Must have
• Bold, clean style

```html
<!DOCTYPE html>
<html lang="en">
<head>
<meta charset="utf-8">
<title>Quillbright – Say Goodbye to Paper Cuts</title>
<link rel="stylesheet" href="https://fonts.googleapis.com/css2?family=Mulish:wght@400;500;600;700&display=swap">
<style>
  :root {
    --paper: #ffffff;
    --navy: #1f2e4d;
    --grey-text: #5a5a5a;
    --link-blue: #2e6bb4;
    --skin-light: #f6dcc6;
    --skin-mid: #f0c7a8;
    --bandage: #f3c99a;
  }
  * { margin: 0; padding: 0; box-sizing: border-box; }
  html, body {
    width: 958px;
    height: 1200px;
    overflow: hidden;
    background: var(--paper);
  }
  .ad {
    position: relative;
    width: 958px;
    height: 1200px;
    background: var(--paper);
    font-family: "Mulish", sans-serif;
    color: var(--navy);
    overflow: hidden;
  }
  .headline {
    position: absolute;
    left: 40px;
    top: 50px;
    font-size: 101px;
    font-weight: 500;
    line-height: 104px;
    letter-spacing: -0.5px;
    color: var(--navy);
    z-index: 3;
  }
  .hero-photo {
    position: absolute;
    left: 0;
    top: 255px;
    width: 958px;
    height: 735px;
    z-index: 1;
  }
  .tagline {
    position: absolute;
    left: 40px;
    top: 990px;
    font-size: 38px;
    font-weight: 500;
    line-height: 44px;
    color: var(--navy);
    white-space: nowrap;
    z-index: 3;
  }
  .discover {
    position: absolute;
    left: 40px;
    top: 1112px;
    font-size: 21px;
    font-weight: 400;
    color: var(--grey-text);
    white-space: nowrap;
    z-index: 3;
  }
  .website {
    position: absolute;
    left: 40px;
    top: 1134px;
    font-size: 28px;
    font-weight: 500;
    color: var(--link-blue);
    white-space: nowrap;
    z-index: 3;
  }
  .brand {
    position: absolute;
    left: 597px;
    width: 310px;
    top: 1006px;
    display: flex;
    flex-direction: column;
    align-items: center;
    gap: 10px;
    z-index: 3;
  }
  .brand-square {
    width: 80px;
    height: 80px;
    background: var(--navy);
  }
  .brand-name {
    font-size: 62px;
    font-weight: 700;
    line-height: 1;
    color: var(--navy);
    white-space: nowrap;
  }
</style>
</head>
<body>
  <main class="ad">
    <h1 class="headline">Say Goodbye to<br>Paper Cuts</h1>

    <svg class="hero-photo" role="img" aria-label="Photo of two hands applying an adhesive bandage to a fingertip" viewBox="0 0 958 735" preserveAspectRatio="none">
      <defs>
        <radialGradient id="hand-right" cx="0.78" cy="0.45" r="0.45">
          <stop offset="0" stop-color="var(--skin-mid)"/>
          <stop offset="0.6" stop-color="var(--skin-light)"/>
          <stop offset="1" stop-color="#ffffff" stop-opacity="0"/>
        </radialGradient>
        <radialGradient id="hand-left" cx="0.25" cy="0.62" r="0.32">
          <stop offset="0" stop-color="var(--bandage)"/>
          <stop offset="0.6" stop-color="var(--skin-light)"/>
          <stop offset="1" stop-color="#ffffff" stop-opacity="0"/>
        </radialGradient>
      </defs>
      <rect width="958" height="735" fill="var(--paper)"/>
      <rect width="958" height="735" fill="url(#hand-right)"/>
      <rect width="958" height="735" fill="url(#hand-left)"/>
    </svg>

    <p class="tagline">On-Demand Admin Support<br>for Mortgage Professionals</p>
    <p class="discover">Discover what we're doing at Quillbright</p>
    <p class="website">www.quillbright.ca</p>

    <div class="brand">
      <div class="brand-square"></div>
      <span class="brand-name">Quillbright</span>
    </div>
  </main>
</body>
</html>
```